Biz Card for Harrowfield Property Partners - HWPP

Harrowfield Property Partners is a commercial real estate acquisitions firm. We buy commercial property and need to raise capital from investors for each deal we buy. The vibe needs to be: give us your money, we will multiply it.
Our website: www.hrwpp-example.com
Competitors are: https://velmarholdings-example.com/, https://tribanquepartners-example.com/, http://www.ostrellecapital-example.com/
Target Market(s)
High Net Worth Individuals, Bankers, Insurance Companies, Commercial Real Estate Brokers.
Industry/Entity Type
Investment Banking
Contact Information for Business Card
Name, Title, Addess, Cell#, Office#, email, website
Requirements
Must have
- use one of our logos. See website for look and feel: www.hrwpp-example.com
Nice to have
- see website: www.hrwpp-example.com

```html
<!DOCTYPE html>
<html lang="en">
<head>
<meta charset="utf-8">
<title>Harrowfield Property Partners – Business Card</title>
<link href="https://fonts.googleapis.com/css2?family=Open+Sans:wght@300;400;700&display=swap" rel="stylesheet">
<style>
  :root {
    --backdrop: #3a332f;
    --card: #1c1c1c;
    --card-edge: #151515;
    --emboss: #141414;
    --emboss-text: #262626;
    --ink: #ffffff;
    --ink-soft: #e8e8e8;
    --ink-muted: #9a9a9a;
    --rule: #d0d0d0;
  }
  * { margin: 0; padding: 0; box-sizing: border-box; }
  html, body {
    width: 1200px; height: 847px; overflow: hidden;
    background: var(--backdrop);
    font-family: "Open Sans", Arial, sans-serif;
  }
  .stage {
    position: relative; width: 1200px; height: 847px;
    display: flex; align-items: center; justify-content: center; gap: 40px;
  }
  .card {
    position: relative; width: 540px; height: 309px;
    background: var(--card);
    box-shadow: 0 12px 30px rgba(0,0,0,.45);
    border: 1px solid var(--card-edge);
  }
  /* back side */
  .card-back .mark {
    position: absolute; left: 50%; top: 58px; transform: translateX(-50%);
    display: flex; flex-direction: column; align-items: center; gap: 14px;
  }
  .card-back .mark-circle {
    width: 96px; height: 96px; border-radius: 50%;
    background: var(--emboss);
    box-shadow: inset 1px 1px 2px rgba(255,255,255,.06), inset -1px -2px 3px rgba(0,0,0,.5);
  }
  .card-back .mark-name {
    color: var(--emboss-text); font-weight: 400; font-size: 15px; letter-spacing: 4px;
  }
  /* front side */
  .brand {
    position: absolute; left: 26px; top: 106px;
    display: flex; align-items: center; gap: 10px;
  }
  .brand-circle { width: 48px; height: 48px; border-radius: 50%; background: var(--ink); }
  .brand-name {
    color: var(--ink); font-weight: 400; font-size: 19px; letter-spacing: 3px; line-height: 1;
  }
  .brand-sub {
    display: block; margin-top: 5px;
    color: var(--ink-muted); font-weight: 400; font-size: 7.5px; letter-spacing: 2.2px;
  }
  .divider {
    position: absolute; left: 298px; top: 70px; width: 1px; height: 170px; background: var(--rule);
  }
  .contact { position: absolute; left: 314px; top: 72px; color: var(--ink-soft); }
  .contact-name { color: var(--ink); font-weight: 700; font-size: 16px; line-height: 1.1; }
  .contact-title { font-size: 11.5px; margin-bottom: 8px; }
  .contact-address { font-size: 11.5px; line-height: 1.35; margin-bottom: 8px; }
  .contact-list { list-style: none; font-size: 11.5px; line-height: 1.4; }
  .contact-list li { display: flex; align-items: center; gap: 6px; }
  .contact-list svg { width: 10px; height: 10px; fill: var(--ink); flex: none; }
</style>
</head>
<body>
<main class="stage">
  <section class="card card-back" aria-label="Card back">
    <div class="mark">
      <div class="mark-circle"></div>
      <span class="mark-name">HARROWFIELD</span>
    </div>
  </section>

  <section class="card card-front" aria-label="Card front">
    <div class="brand">
      <div class="brand-circle"></div>
      <div>
        <span class="brand-name">HARROWFIELD</span>
        <span class="brand-sub">PROPERTY PARTNERS</span>
      </div>
    </div>
    <div class="divider"></div>
    <div class="contact">
      <p class="contact-name">DANIEL ASHCOMBE</p>
      <p class="contact-title">President</p>
      <p class="contact-address">48 Marlow Crescent, Suite 1205<br>Westbrook, FL 33190</p>
      <ul class="contact-list">
        <li><svg viewBox="0 0 10 10"><path d="M2.5 0h5a.8.8 0 0 1 .8.8v8.4a.8.8 0 0 1-.8.8h-5a.8.8 0 0 1-.8-.8V.8A.8.8 0 0 1 2.5 0zm.5 1.2v6.6h4V1.2z"/></svg>(555) 014-2286</li>
        <li><svg viewBox="0 0 10 10"><path d="M2 .5l1.6 2-1 1.1a6 6 0 0 0 3.8 3.8l1.1-1 2 1.6-1.2 1.5C5 9.3.7 5 .5 1.7z"/></svg>(555) 014-2287</li>
        <li><svg viewBox="0 0 10 10"><path d="M0 2h10v6H0zm.9.8L5 5.6l4.1-2.8z" fill-rule="evenodd"/></svg>info@hrwpp-example.com</li>
        <li><svg viewBox="0 0 10 10"><path d="M5 0a5 5 0 1 0 0 10A5 5 0 0 0 5 0zm0 1.2c.7.7 1.1 2 1.2 3.2H3.8C3.9 3.2 4.3 1.9 5 1.2zM3.8 5.6h2.4C6.1 6.8 5.7 8.1 5 8.8c-.7-.7-1.1-2-1.2-3.2z"/></svg>www.hrwpp-example.com</li>
      </ul>
    </div>
  </section>
</main>
</body>
</html>
```